Corvane Networks web design

Corvane is an Internet Service Provider bringing high-speed service to homes and businesses. Our principal market target is rural areas of West Michigan, but we intend to expand rapidly. We need a website to market our services, facilitate online ordering, customer support and communicate with our customers.

I will upload a draft outline of the content we hope to include in the website.

We compete directly with Halberd Communications, Lumetra, Dravix and Kelwick communications to bring Internet service to homes and businesses in our coverage area.

Our primary values include:

1. Unlike our competitors, we do not require long term contractors or service bundles; There are no termination fees, for example. All services are sold on a recurring 1-month agreement term.
2. Unlike other wireless (mobile) providers, we do not limit downloads or uploads with bit/byte buckets
3. We provide service to areas ignored by the larger carriers - Rural areas in Michigan that lack options for broadband are prime targets for Corvane to cover.
4. Unlike other wireless ISP's, we utilize licensed FCC spectrum. We do not use unlicensed/free frequencies, providing us an advantage for reliability and stability.
Updates

So many wonderful designs, thank you very much for all your hard work. We are evaluating all our favorite designs and plan to make a selection in the next 2 days. I will be in touch with you to request revisions if necessary or further refinements.  Thank you again for your efforts on this project.

Target Market(s)

Our target market is home Internet users. however, that does not mean that our users are "high tech" oriented - they are just normal mom's and pop's who buy Internet for home use. The site should be easy to navigate and communicate our message of speed, value, reliability and facilitate simple product ordering.

Industry/Entity Type

Internet

Requirements
Must have
• Our phone number should be prominently displayed 1-844-7NU-LINK
• Our logo is uploaded in the attachments.
• Design for desktop and mobile devices.
Nice to have
• The most modern of web design trends. Such as a design that facilitates parallax scrolling effects rather than lots of individual pages.
• Stock artwork communicating our values of speed and reliability.

```html
<!DOCTYPE html>
<html lang="en">
<head>
<meta charset="utf-8">
<title>Corvane Networks – West Michigan's Best Internet Service</title>
<link rel="stylesheet" href="https://fonts.googleapis.com/css2?family=Open+Sans:wght@400;600;700;800&display=swap">
<style>
:root{
  --orange:#f58220;
  --ink:#333333;
  --muted:#666666;
  --line:#dddddd;
  --white:#ffffff;
  --hero-dark:#2a2b2d;
  --cover-box:rgba(20,32,48,.88);
  --teal:#1aa3d4;
  --plan-card:#333333;
  --plan-head:#3d3d3d;
  --band:#f4f4f4;
  --footer:#ececec;
  --footer-bar:#e2e2e2;
  --arrow:#3b3b3b;
}
*{box-sizing:border-box;margin:0;padding:0}
html,body{width:1200px;height:3126px;overflow:hidden}
body{font-family:"Open Sans",Arial,sans-serif;color:var(--ink);background:var(--white);position:relative}
.abs{position:absolute}
a{color:inherit;text-decoration:none}

/* utility bar */
.utility{position:absolute;top:0;left:0;width:1200px;height:38px;background:var(--white);border-bottom:1px solid #eee}
.utility-link{position:absolute;top:0;height:38px;display:flex;align-items:center;gap:5px;padding:0 8px;border-left:1px solid #eee;font-size:10px;font-weight:600;color:#777;letter-spacing:.3px;white-space:nowrap}
.search{position:absolute;left:786px;top:0;width:126px;height:38px;display:flex}
.search span{flex:1;font-size:10px;color:#999;padding:12px 6px;border-left:1px solid #eee;white-space:nowrap}
.search b{width:38px;height:38px;background:var(--orange);display:flex;align-items:center;justify-content:center;flex:none}

/* nav */
.navbar{position:absolute;top:38px;left:0;width:1200px;height:63px;background:var(--white);box-shadow:0 1px 2px rgba(0,0,0,.08)}
.brand{position:absolute;left:288px;top:22px;display:flex;align-items:center;gap:7px;font-weight:800;font-size:14px;color:var(--orange);letter-spacing:.4px;white-space:nowrap}
.brand i{width:10px;height:10px;border-radius:50%;background:var(--orange);display:block}
.menu{position:absolute;top:24px;font-size:14px;color:#444;white-space:nowrap}
.menu.active{color:var(--orange)}

/* hero */
.hero{position:absolute;top:101px;left:0;width:1200px;height:579px;background:radial-gradient(ellipse at 70% 40%,#5a5e56 0%,#3a3b3a 40%,var(--hero-dark) 80%)}
.hero-title{position:absolute;top:68px;left:0;width:1200px;text-align:center;color:var(--white);font-size:33px;font-weight:700}
.cover{position:absolute;left:303px;top:240px;width:245px;height:241px;background:var(--cover-box);color:var(--white);padding:22px 18px}
.cover h3{font-size:19px;font-weight:700;letter-spacing:.5px}
.cover p{font-size:14px;line-height:19px;margin-top:22px}
.cover .field{height:44px;background:var(--white);margin-top:18px;color:#aaa;font-size:12px;padding:14px 10px}
.cover .go{height:44px;background:var(--teal);margin-top:10px;text-align:center;font-weight:700;font-size:14px;line-height:44px;letter-spacing:.5px}
.or{position:absolute;left:560px;top:408px;color:var(--white);font-size:19px;font-weight:700}
.why{position:absolute;left:649px;top:163px;color:var(--white)}
.why h3{font-size:25px;font-weight:700}
.why li{list-style:none;display:flex;align-items:center;gap:16px;font-size:23px;margin-top:8px}
.order{position:absolute;left:652px;top:366px;width:260px;height:122px;background:var(--orange);color:var(--white);padding:16px 22px}
.order .l1{font-size:24px;font-weight:400}
.order .l2{font-size:28px;font-weight:700;margin-top:10px}

/* intro slider */
.intro{position:absolute;top:680px;left:0;width:1200px;height:506px;border-bottom:1px solid var(--line)}
.sec-title{position:absolute;left:288px;font-size:21px;font-weight:700;color:#333;letter-spacing:.3px}
.intro p{position:absolute;left:288px;top:120px;width:350px;font-size:13px;line-height:17px;color:#555}
.perks{position:absolute;left:288px;top:215px;list-style:none}
.perks li{display:flex;align-items:center;gap:10px;font-size:13px;color:#555;height:26px}
.photo-circle{position:absolute;left:642px;top:95px;width:264px;height:264px;border-radius:50%;background:radial-gradient(circle at 40% 45%,#7fd8f0 0%,#1e8fc0 35%,#0c3a5c 70%,#06182a 100%)}
.arrow{position:absolute;top:222px;width:53px;height:55px;background:var(--arrow);display:flex;align-items:center;justify-content:center}
.pager{position:absolute;left:517px;top:453px;display:flex}
.pager span{width:55px;height:53px;background:#444;color:var(--white);font-size:22px;display:flex;align-items:center;justify-content:center}
.pager span.on{background:var(--orange)}

/* plans */
.plans{position:absolute;top:1186px;left:0;width:1200px;height:534px;border-bottom:1px solid var(--line)}
.plans-copy{position:absolute;left:288px;top:172px;width:205px;font-size:12.5px;line-height:17px;color:#555}
.plans-copy p+p{margin-top:12px}
.btn-plans{position:absolute;left:288px;top:370px;width:210px;height:46px;background:var(--teal);color:var(--white);font-weight:700;font-size:14px;text-align:center;line-height:46px;letter-spacing:.5px}
.plan{position:absolute;top:173px;width:198px;height:238px;background:var(--plan-card);color:var(--white)}
.plan h4{height:65px;background:var(--plan-head);border-bottom:1px solid #555;font-size:18px;font-weight:400;text-align:center;line-height:65px}
.plan .price{padding:18px 17px 10px;font-size:22px;font-weight:700;border-bottom:1px solid #4a4a4a}
.plan .price small{font-size:10px;font-weight:400}
.plan ul{list-style:none;padding:10px 14px;font-size:10.5px;line-height:26px;white-space:nowrap}

/* news / blog / tweets band */
.band{position:absolute;top:1720px;left:0;width:1200px;height:950px;background:var(--band)}
.card{position:absolute;width:195px;background:var(--white);box-shadow:0 1px 3px rgba(0,0,0,.15)}
.card .pic{height:115px;background:linear-gradient(135deg,#0c2a66 0%,#2a66c4 45%,#6f9fe0 55%,#0e2d6a 100%)}
.card .body{display:flex;padding:10px 8px;gap:8px}
.card .date{width:36px;font-size:10px;font-weight:700;line-height:12px;flex:none}
.card .date small{display:block;font-size:7px;font-weight:400;color:#888;margin-top:4px}
.card .date em{font-style:normal;color:var(--orange)}
.card h5{font-size:13px;font-weight:600;line-height:16px;color:#333}
.card .ex{font-size:8px;line-height:10px;color:#888;margin-top:8px}
.tw{text-align:center;font-size:9px;color:#aaa;padding-top:12px}
.tw-name{font-size:9px;font-weight:700}

/* footer */
.footer{position:absolute;top:2670px;left:0;width:1200px;height:420px;background:var(--footer)}
.f-links{position:absolute;left:288px;top:52px;list-style:none;font-size:11px;line-height:17px;color:#555}
.f-col{position:absolute;font-size:11px;line-height:17px;color:#555}
.f-col b{font-weight:700;color:#333}
.call{position:absolute;left:0;width:1200px;text-align:center}
.bottom{position:absolute;top:3090px;left:0;width:1200px;height:36px;background:var(--footer-bar);font-size:11px;color:#666}
</style>
</head>
<body>

<header class="utility">
  <a class="utility-link" style="left:528px" href="#"><svg width="11" height="11" viewBox="0 0 12 12"><rect x="1" y="2" width="10" height="8" fill="none" stroke="#888" stroke-width="1.4"/></svg>BLOG</a>
  <a class="utility-link" style="left:606px" href="#"><svg width="11" height="11" viewBox="0 0 12 12"><circle cx="4" cy="4" r="2.2" fill="#888"/><circle cx="8.5" cy="4.5" r="2" fill="#888"/><rect x="1" y="7" width="10" height="4" rx="2" fill="#888"/></svg>CUSTOMERS</a>
  <a class="utility-link" style="left:702px" href="#"><svg width="11" height="11" viewBox="0 0 12 12"><circle cx="6" cy="4" r="2.6" fill="#888"/><rect x="1.5" y="7.5" width="9" height="4" rx="2" fill="#888"/></svg>ACCOUNT</a>
  <div class="search"><span>Search...</span><b><svg width="14" height="14" viewBox="0 0 14 14"><circle cx="6" cy="6" r="4" fill="none" stroke="#fff" stroke-width="2"/><line x1="9" y1="9" x2="13" y2="13" stroke="#fff" stroke-width="2"/></svg></b></div>
</header>

<nav class="navbar">
  <div class="brand"><i></i>CORVANE NETWORKS</div>
  <a class="menu active" style="left:515px" href="#">Home</a>
  <a class="menu" style="left:599px" href="#">Service Plans</a>
  <a class="menu" style="left:722px" href="#">Coverage Map</a>
  <a class="menu" style="left:844px" href="#">About us</a>
</nav>

<section class="hero" role="img" aria-label="Background photo of a family relaxing in front of a television at home">
  <h1 class="hero-title">West Michigan's Best Internet Service</h1>
  <form class="cover">
    <h3>AM I COVERED?</h3>
    <p>Enter &nbsp;Your address to check for service availability</p>
    <div class="field">Enter your address...</div>
    <div class="go">SUBMIT</div>
  </form>
  <div class="or">- OR -</div>
  <div class="why">
    <h3>Why we're better?</h3>
    <ul>
      <li><svg width="20" height="20" viewBox="0 0 20 20"><circle cx="10" cy="11" r="7.5" fill="none" stroke="#fff" stroke-width="1.8"/><line x1="10" y1="11" x2="10" y2="6.5" stroke="#fff" stroke-width="1.8"/><rect x="8" y="1" width="4" height="2" fill="#fff"/></svg>Faster Speed</li>
      <li><svg width="20" height="20" viewBox="0 0 20 20"><circle cx="10" cy="10" r="8" fill="none" stroke="#fff" stroke-width="1.8"/><line x1="4.5" y1="4.5" x2="15.5" y2="15.5" stroke="#fff" stroke-width="1.8"/></svg>No Limits</li>
      <li><svg width="20" height="20" viewBox="0 0 20 20"><path d="M3 9h3v9H3zM7 9l4-7c2 0 2 2 1.5 4H17c1 0 1.5 1 1.2 2l-2 8c-.2.7-.8 1-1.5 1H7z" fill="#fff"/></svg>More Value</li>
    </ul>
  </div>
  <div class="order"><div class="l1">ORDER NOW</div><div class="l2">844-7NU-LINK</div></div>
</section>

<section class="intro">
  <h2 class="sec-title" style="top:50px">WEST MICHIGAN'S BEST INTERNET SERVICE</h2>
  <p>Corvane Networks is a Michigan-based company providing high-speed Internet services to West Michigan homes and businesses.</p>
  <ul class="perks">
    <li><svg width="13" height="13" viewBox="0 0 10 10"><path d="M5 0l1.5 3.2L10 3.6 7.4 6l.7 3.5L5 7.8 1.9 9.5 2.6 6 0 3.6l3.5-.4z" fill="var(--orange)"/></svg>Honest Pricing, No Hidden Fees</li>
    <li><svg width="13" height="13" viewBox="0 0 10 10"><path d="M5 0l1.5 3.2L10 3.6 7.4 6l.7 3.5L5 7.8 1.9 9.5 2.6 6 0 3.6l3.5-.4z" fill="var(--orange)"/></svg>No Long Term Contracts</li>
    <li><svg width="13" height="13" viewBox="0 0 10 10"><path d="M5 0l1.5 3.2L10 3.6 7.4 6l.7 3.5L5 7.8 1.9 9.5 2.6 6 0 3.6l3.5-.4z" fill="var(--orange)"/></svg>No Phone Line or Cable TV required</li>
    <li><svg width="13" height="13" viewBox="0 0 10 10"><path d="M5 0l1.5 3.2L10 3.6 7.4 6l.7 3.5L5 7.8 1.9 9.5 2.6 6 0 3.6l3.5-.4z" fill="var(--orange)"/></svg>100% Satisfaction Guaranteed</li>
    <li><svg width="13" height="13" viewBox="0 0 10 10"><path d="M5 0l1.5 3.2L10 3.6 7.4 6l.7 3.5L5 7.8 1.9 9.5 2.6 6 0 3.6l3.5-.4z" fill="var(--orange)"/></svg>Fast, Superior Performance in your home and business</li>
    <li><svg width="13" height="13" viewBox="0 0 10 10"><path d="M5 0l1.5 3.2L10 3.6 7.4 6l.7 3.5L5 7.8 1.9 9.5 2.6 6 0 3.6l3.5-.4z" fill="var(--orange)"/></svg>Interference-Free FCC Licensed 4G Coverage</li>
  </ul>
  <div class="photo-circle" role="img" aria-label="Close-up photo of a glowing blue internet speed test gauge"></div>
  <div class="arrow" style="left:0"><svg width="18" height="28" viewBox="0 0 18 28"><path d="M15 2L3 14l12 12" fill="none" stroke="#fff" stroke-width="3"/></svg></div>
  <div class="arrow" style="left:1147px"><svg width="18" height="28" viewBox="0 0 18 28"><path d="M3 2l12 12L3 26" fill="none" stroke="#fff" stroke-width="3"/></svg></div>
  <div class="pager"><span class="on">1</span><span>2</span><span>3</span></div>
</section>

<section class="plans">
  <h2 class="sec-title" style="top:96px">SERVICE PLANS</h2>
  <div class="plans-copy">
    <p>All <b>Residential</b> packages include: Up to 5 Cloud Mail enabled email accounts and unlimited download and upload – ie, "no bit buckets"</p>
    <p>All <b>Business</b> packages include: Static IP address included for free and unlimited download and upload – ie, "no bit buckets"</p>
  </div>
  <a class="btn-plans" href="#">VIEW ALL PLANS</a>
  <div class="plan" style="left:507px">
    <h4>Residential Plans</h4>
    <div class="price">$24.99 <small>per month</small></div>
    <ul><li>Up to 10 Mb download</li><li>Up to 2.0 Mb upload</li><li>Static IP addresses $15 each</li></ul>
  </div>
  <div class="plan" style="left:714px">
    <h4>Business Plans</h4>
    <div class="price">$74.99 <small>per month</small></div>
    <ul><li>Up to 50 Mb download</li><li>Up to 20 Mb upload</li><li>Add. Static IP addresses $15 each</li></ul>
  </div>
</section>

<section class="band">
  <h2 class="sec-title" style="top:50px">LATEST NEWS</h2>
  <article class="card" style="left:286px;top:113px;height:235px"><div class="pic" role="img" aria-label="Photo of a person walking through a blue-lit server room"></div><div class="body"><div class="date">27 Jan 2014<small>Posted by <em>Admin</em></small></div><div><h5>This is a standard post format with preview picture</h5><div class="ex">Lorem ipsum dolor sit amet, consectetur adipiscing elit. Nulla bibendum.</div></div></div></article>
  <article class="card" style="left:505px;top:113px;height:235px"><div class="pic" role="img" aria-label="Photo of a person walking through a blue-lit server room"></div><div class="body"><div class="date">27 Jan 2014<small>Posted by <em>Admin</em></small></div><div><h5>This is a standard post format with preview picture</h5><div class="ex">Lorem ipsum dolor sit amet, consectetur adipiscing elit. Nulla bibendum.</div></div></div></article>
  <article class="card" style="left:719px;top:113px;height:235px"><div class="pic" role="img" aria-label="Photo of a person walking through a blue-lit server room"></div><div class="body"><div class="date">27 Jan 2014<small>Posted by <em>Admin</em></small></div><div><h5>This is a standard post format with preview picture</h5><div class="ex">Lorem ipsum dolor sit amet, consectetur adipiscing elit. Nulla bibendum.</div></div></div></article>

  <h2 class="sec-title" style="top:440px">FROM OUR BLOG</h2>
  <article class="card" style="left:286px;top:480px;height:130px"><div class="body"><div class="date">27 Jan 2014<small>Posted by <em>Admin</em></small></div><div><h5>This is a standard blog format post</h5><div class="ex">Lorem ipsum dolor sit amet, consectetur adipiscing elit. Nulla bibendum mi vel tellus, non gravida lorem vehicula.</div></div></div></article>
  <article class="card" style="left:505px;top:480px;height:130px"><div class="body"><div class="date">27 Jan 2014<small>Posted by <em>Admin</em></small></div><div><h5>This is a standard blog format post a little bit longer</h5><div class="ex">Lorem ipsum dolor sit amet, consectetur adipiscing elit. Nulla bibendum mi vel tellus, non gravida lorem vehicula.</div></div></div></article>
  <article class="card" style="left:719px;top:480px;height:130px"><div class="body"><div class="date">27 Jan 2014<small>Posted by <em>Admin</em></small></div><div><h5>This is a standard blog format without preview picture</h5><div class="ex">Lorem ipsum dolor sit amet, consectetur adipiscing elit. Nulla bibendum mi vel tellus, non gravida lorem vehicula.</div></div></div></article>

  <h2 class="sec-title" style="top:690px">LATEST TWEETS</h2>
  <article class="card" style="left:286px;top:740px;height:135px"><div class="tw">3P</div><div class="body"><div class="date">27 Jan 2014</div><div><div class="tw-name">John Doe</div><div class="ex">Quick update on our network: new towers now live across the lakeshore. #fastinternet</div></div></div></article>
  <article class="card" style="left:505px;top:740px;height:135px"><div class="tw">3P</div><div class="body"><div class="date">27 Jan 2014</div><div><div class="tw-name">John Doe</div><div class="ex">Quick update on our network: new towers now live across the lakeshore. #fastinternet</div></div></div></article>
  <article class="card" style="left:719px;top:740px;height:135px"><div class="tw">3P</div><div class="body"><div class="date">27 Jan 2014</div><div><div class="tw-name">John Doe</div><div class="ex">Quick update on our network: new towers now live across the lakeshore. #fastinternet</div></div></div></article>
</section>

<footer class="footer">
  <ul class="f-links">
    <li>Service Plans</li><li>Coverage Map</li><li>Who is Corvane</li><li>Company Blog</li><li>Customer Support</li><li>Account Management</li>
  </ul>
  <svg class="abs" style="left:505px;top:50px" width="34" height="34" viewBox="0 0 34 34"><circle cx="17" cy="17" r="14" fill="none" stroke="#444" stroke-width="3"/><path d="M17 9v8l6 4" fill="none" stroke="#444" stroke-width="3"/></svg>
  <div class="f-col" style="left:556px;top:50px"><b>Support Staff Hours</b><br>Weekdays 7am to 10pm<br>Weekends 8am to 5pm<br>Holiday scheduling varies</div>
  <svg class="abs" style="left:507px;top:160px" width="30" height="28" viewBox="0 0 30 28"><path d="M1 13L29 1 23 27 15 19 25 6 11 17z" fill="#444"/></svg>
  <div class="f-col" style="left:556px;top:160px">Email support<br><b>support@corvanelink.net</b></div>
  <svg class="abs" style="left:738px;top:50px" width="24" height="34" viewBox="0 0 24 34"><path d="M12 0C5 0 0 5 0 12c0 9 12 22 12 22s12-13 12-22C24 5 19 0 12 0z" fill="#444"/><circle cx="12" cy="12" r="4.5" fill="var(--footer)"/></svg>
  <div class="f-col" style="left:786px;top:50px"><b>Corvane Networks, LLC</b><br>1175 Alder Row Avenue<br>Holt Ridge, MI 49870</div>
  <div class="call" style="top:263px;font-size:16px;color:#555">Call today to place an order or reach customer support</div>
  <div class="call" style="top:286px;font-size:22px;font-weight:600;color:var(--orange);letter-spacing:1px">844 - 7NU - LINK</div>
  <div class="call" style="top:342px;font-size:12px;color:#555;line-height:18px">Local number<br>517-555-0142</div>
</footer>

<div class="bottom">
  <span class="abs" style="left:288px;top:11px">© 2014 Corvane Networks, LLC. All Rights Reserved</span>
  <span class="abs" style="left:740px;top:11px">Proud to live and work in Michigan!</span>
</div>

</body>
</html>
```